Looking for a creative label design for our retail coffee bags

We are a coffee manufacturer (coffee roaster) looking to re-brand our retail label for our coffee bags. Our main coffee blend that we sell is our Harborline Velvet Blend. You can use this name when creating the label. We are going for a look that represents our company as a coffee roaster. Please reference our website (www.brindlemugworks.com) and our Facebook page to learn more about our company and to give you more inspiration on creating this design.

Target Market(s)

Retail customers/grocery stores

Industry/Entity Type

Manufacturer

Requirements
Must have
• The size of the label has to be 3" width x 4" height

Logo must be Black
Nice to have
• We currently incorporate a color on our labels for each blend. For example, Harborline Velvet Blend (royal blue), Decaffeinated Blend (red), Breakfast Blend (green), Flavored coffees (gold).

Rustic/vintage style

```html
<!DOCTYPE html>
<html lang="en">
<head>
<meta charset="utf-8">
<title>Brindle Mugworks – Harborline Velvet Blend Label</title>
<link rel="stylesheet" href="https://fonts.googleapis.com/css2?family=Poiret+One&family=Sacramento&display=swap">
<style>
  :root {
    --backdrop: #0b0b0b;
    --label-black: #231f20;
    --stripe-grey: #3b3a3b;
    --blend-red: #ec1c24;
    --blend-red-deep: #dd1820;
    --ink-white: #ffffff;
  }
  html, body {
    margin: 0;
    padding: 0;
    width: 1200px;
    height: 1200px;
    overflow: hidden;
    background: var(--backdrop);
  }
  .canvas {
    position: relative;
    width: 1200px;
    height: 1200px;
  }
  .label {
    position: absolute;
    left: 250px;
    top: 100px;
    width: 700px;
    height: 1000px;
    background: var(--label-black);
    overflow: hidden;
  }
  .side-column {
    position: absolute;
    top: 0;
    width: 140px;
    height: 1000px;
    background: var(--label-black);
  }
  .side-column--left { left: 0; }
  .side-column--right { right: 0; }
  .side-stripes {
    position: absolute;
    left: 0;
    top: 590px;
    width: 140px;
    height: 410px;
  }
  .blend-band {
    position: absolute;
    left: 140px;
    top: 0;
    width: 420px;
    height: 1000px;
    background: var(--blend-red);
  }
  .bean-texture {
    position: absolute;
    left: 0;
    top: 660px;
    width: 420px;
    height: 320px;
    background: radial-gradient(ellipse at center, var(--blend-red-deep) 0%, var(--blend-red) 75%);
  }
  .brand-seal {
    position: absolute;
    left: 40px;
    top: 96px;
    width: 340px;
    height: 340px;
    border-radius: 50%;
    background: var(--label-black);
    display: flex;
    align-items: center;
    justify-content: center;
    box-sizing: border-box;
  }
  .brand-seal::after {
    content: "";
    position: absolute;
    inset: 12px;
    border: 1.5px solid rgba(255,255,255,0.6);
    border-radius: 50%;
  }
  .brand-name {
    margin: 0;
    font-family: "Poiret One", sans-serif;
    font-weight: 400;
    font-size: 56px;
    line-height: 1.05;
    color: var(--ink-white);
    text-align: center;
    letter-spacing: 1px;
  }
  .roast-note {
    position: absolute;
    left: 0;
    width: 420px;
    top: 528px;
    margin: 0;
    text-align: center;
    font-family: "Sacramento", cursive;
    font-size: 78px;
    line-height: 1;
    color: var(--ink-white);
  }
  .blend-name {
    position: absolute;
    left: 0;
    width: 420px;
    top: 650px;
    margin: 0;
    text-align: center;
    font-family: "Poiret One", sans-serif;
    font-weight: 400;
    font-size: 56px;
    line-height: 76px;
    color: var(--ink-white);
    text-transform: uppercase;
  }
</style>
</head>
<body>
<main class="canvas">
  <section class="label">
    <div class="side-column side-column--left">
      <svg class="side-stripes" viewBox="0 0 140 410" width="140" height="410" aria-hidden="true">
        <g fill="var(--stripe-grey)">
          <rect x="0" y="0" width="140" height="22"/>
          <rect x="0" y="46" width="140" height="22"/>
          <rect x="0" y="92" width="140" height="22"/>
          <rect x="0" y="138" width="140" height="22"/>
          <rect x="0" y="184" width="140" height="22"/>
          <rect x="0" y="230" width="140" height="22"/>
          <rect x="0" y="276" width="140" height="22"/>
          <rect x="0" y="322" width="140" height="22"/>
          <rect x="0" y="368" width="140" height="22"/>
        </g>
      </svg>
    </div>

    <div class="blend-band">
      <div class="bean-texture" role="img" aria-label="Faint coffee bean pattern behind the blend name"></div>
      <div class="brand-seal">
        <p class="brand-name">Brindle<br>Mugworks</p>
      </div>
      <p class="roast-note">fresh roasted</p>
      <h1 class="blend-name">Harborline<br>Velvet<br>Blend</h1>
    </div>

    <div class="side-column side-column--right">
      <svg class="side-stripes" viewBox="0 0 140 410" width="140" height="410" aria-hidden="true">
        <g fill="var(--stripe-grey)">
          <rect x="0" y="0" width="140" height="22"/>
          <rect x="0" y="46" width="140" height="22"/>
          <rect x="0" y="92" width="140" height="22"/>
          <rect x="0" y="138" width="140" height="22"/>
          <rect x="0" y="184" width="140" height="22"/>
          <rect x="0" y="230" width="140" height="22"/>
          <rect x="0" y="276" width="140" height="22"/>
          <rect x="0" y="322" width="140" height="22"/>
          <rect x="0" y="368" width="140" height="22"/>
        </g>
      </svg>
    </div>
  </section>
</main>
</body>
</html>
```